U.S. Popcorn company needs business cards

We are a popcorn company that manufactures popcorn and sells it to grocery stores worldwide. Our theme is "Americana" and our logo is U.S. route 66 which is the most famous highway in the U.S.

We would like the design to be simple and to use both sides. On the back side we would like to see just the logo and website. The front would be normal details

Target Market(s)

Wholesalers, grocers and distributors

Industry/Entity Type

Manufacture

Contact Information for Business Card

Business name: Bluebell Ridge Popcorn
Phone: +1 555 014 2286
Email: Derek@bluebellridgepopcorn.com
website: www.bluebellridgepopcorn.com
Tag Line: "POPular for a reason"
Name: Derek Halvorsen
Title: Founder/President

Requirements
Must have
• Either this design should be fun or clean and simple. I will let you show me your thougths.
Nice to have
• Anything that ties in the real Hwy Route 66.
• Colors might need to be red, white and blue incorporated.
Should not have
• Not be too busy.

```html
<!DOCTYPE html>
<html lang="en">
<head>
<meta charset="utf-8">
<title>Bluebell Ridge Popcorn – Business Card</title>
<link rel="stylesheet" href="https://fonts.googleapis.com/css2?family=Lato:wght@400;700;900&display=swap">
<style>
  :root {
    --navy: #00256a;
    --red: #e31e24;
    --white: #ffffff;
    --page: #ececec;
    --photo-light: #f1ede8;
    --photo-mid: #e2dcd4;
    --photo-warm: #e9d9b2;
  }
  * { margin: 0; padding: 0; box-sizing: border-box; }
  html, body { width: 1200px; height: 586px; overflow: hidden; }
  body {
    background: var(--page);
    font-family: "Lato", sans-serif;
    position: relative;
  }
  .card {
    position: absolute;
    top: 129px;
    width: 501px;
    height: 300px;
    overflow: hidden;
  }
  .card--back { left: 61px; }
  .card--front { left: 619px; background: var(--navy); }

  .product-photo {
    position: absolute;
    inset: 0;
    background:
      radial-gradient(ellipse 75px 135px at 49% 52%, var(--photo-warm), transparent 80%),
      linear-gradient(180deg, var(--photo-light) 0%, var(--photo-mid) 100%);
  }
  .back-brand {
    position: absolute;
    left: 196px;
    top: 146px;
    width: 100px;
    text-align: center;
    color: var(--navy);
    font-weight: 900;
    font-size: 11px;
    line-height: 1.15;
  }
  .back-web {
    position: absolute;
    left: 0;
    right: 0;
    bottom: 14px;
    text-align: center;
    color: var(--navy);
    font-weight: 700;
    font-size: 12px;
  }

  .front-shapes { position: absolute; inset: 0; }

  .contact {
    position: absolute;
    left: 23px;
    top: 0;
    color: var(--white);
  }
  .contact__name {
    position: absolute;
    top: 94px;
    white-space: nowrap;
    color: var(--red);
    font-weight: 900;
    font-size: 16px;
  }
  .contact__title {
    position: absolute;
    top: 117px;
    white-space: nowrap;
    font-size: 11.5px;
  }
  .contact__line {
    position: absolute;
    left: 0;
    display: flex;
    align-items: center;
    gap: 8px;
    white-space: nowrap;
    font-size: 12px;
    font-weight: 700;
  }
  .contact__line--phone { top: 167px; }
  .contact__line--email { top: 191px; }
  .contact__icon { width: 13px; height: 11px; fill: var(--red); }
  .contact__web {
    position: absolute;
    top: 215px;
    white-space: nowrap;
    color: var(--red);
    font-weight: 700;
    font-size: 12px;
  }

  .brand {
    position: absolute;
    left: 309px;
    top: 110px;
    width: 170px;
    text-align: center;
    color: var(--navy);
  }
  .brand__name {
    font-weight: 900;
    font-size: 22px;
    line-height: 1.15;
  }
  .brand__tagline {
    margin-top: 8px;
    color: var(--red);
    font-weight: 700;
    font-size: 11px;
  }
</style>
</head>
<body>

  <section class="card card--back">
    <div class="product-photo" role="img" aria-label="Photo of a red and white striped popcorn box filled with popcorn, standing on a white plate"></div>
    <p class="back-brand">Bluebell Ridge Popcorn</p>
    <p class="back-web">www.bluebellridgepopcorn.com</p>
  </section>

  <section class="card card--front">
    <svg class="front-shapes" viewBox="0 0 501 300" width="501" height="300" aria-hidden="true">
      <path d="M282 0 Q205 150 301 300 L501 300 L501 0 Z" fill="var(--white)"/>
      <path d="M290 0 Q215 160 301 290 Q255 130 361 0 Z" fill="var(--red)"/>
    </svg>

    <div class="contact">
      <p class="contact__name">Derek Halvorsen</p>
      <p class="contact__title">Founder/President</p>
      <p class="contact__line contact__line--phone">
        <svg class="contact__icon" viewBox="0 0 13 11" aria-hidden="true">
          <path d="M1 3 Q6.5 -1 12 3 L11 5 L9 4 L9 3 Q6.5 2 4 3 L4 4 L2 5 Z"/>
          <path d="M3 6 L10 6 L12 10 L1 10 Z"/>
        </svg>
        +1 555 014 2286
      </p>
      <p class="contact__line contact__line--email">
        <svg class="contact__icon" viewBox="0 0 13 11" aria-hidden="true">
          <path d="M0 1 L13 1 L13 10 L0 10 Z M1.5 2.5 L6.5 6.5 L11.5 2.5 L11.5 3.6 L6.5 7.6 L1.5 3.6 Z" fill-rule="evenodd"/>
        </svg>
        Derek@bluebellridgepopcorn.com
      </p>
      <p class="contact__web">www.bluebellridgepopcorn.com</p>
    </div>

    <div class="brand">
      <p class="brand__name">Bluebell Ridge<br>Popcorn</p>
      <p class="brand__tagline">POPular for a reason</p>
    </div>
  </section>

</body>
</html>
```